Design a corporate looking website for Harbourline Funding

Need design only WordPress mock up for Harbourline Funding who provides short term finance solutions to other businesses. We need a corporate looking website that depicts a trustworthy, Dynamic fast acting company.
Visit http://q7.pagemockery.net/ for current mock up We need something like e this but not the same with a design that depicts corporate with more colour and images, needs to install trust and fast action. Please feel free to change the layout as I am not wedded to current design but am happy with what on the landing page.

Target Market(s)

Small to medium sized Businesses

Industry/Entity Type

Finance

Number of Pages Required

1 page

Font styles to use
Sans Serif

Requirements
Must have
• Design Landing pages in WordPress
• Visit http://q7.pagemockery.net/ for current mock up need Layout like this but with a design that depicts corporate with more colour and images, needs to install trust and fast action. Please feel free to change the layout as I am not happy with current design but am wedded to what on the landing page.
Should not have
• any copyright material on it.

```html
<!DOCTYPE html>
<html lang="en">
<head>
<meta charset="utf-8">
<title>Harbourline Funding</title>
<link href="https://fonts.googleapis.com/css2?family=Open+Sans:wght@400;600;700&display=swap" rel="stylesheet">
<style>
:root{
  --blue:#0a9fe0;
  --blue-soft:#4aa9dc;
  --navy:#1a2a4a;
  --nav-bg:#2e3137;
  --green:#47ad4c;
  --red:#e5392e;
  --teal:#16a7d3;
  --grey-btn:#7b7e82;
  --grey-light:#e9edf0;
  --section-grey:#eeeeee;
  --text:#333;
  --muted:#555;
  --white:#fff;
}
*{box-sizing:border-box;margin:0;padding:0}
html,body{width:1200px;height:2932px;overflow:hidden}
body{position:relative;background:var(--white);font-family:"Open Sans",Arial,sans-serif;color:var(--text)}
.abs{position:absolute}

.site-header{left:0;top:0;width:1200px;height:118px;background:var(--white)}
.brand{left:104px;top:34px;display:flex;align-items:center;gap:14px}
.brand-dot{width:40px;height:40px;border-radius:50%;background:var(--blue)}
.brand-name{font-size:27px;font-weight:700;color:var(--navy)}
.search{left:800px;top:39px;width:300px;height:41px;border:1px solid #cfd3d6;border-radius:4px;font-size:13px;color:#999;padding:11px 18px}
.search svg{position:absolute;right:12px;top:11px}

.main-nav{left:0;top:118px;width:1200px;height:60px;background:var(--nav-bg)}
.main-nav a{position:absolute;top:23px;font-size:11px;color:#fff;text-decoration:none;letter-spacing:.2px}
.main-nav a.current{color:var(--blue)}
.main-nav a.current::after{content:"";position:absolute;left:0;right:0;top:25px;height:3px;background:var(--blue)}

.banner{left:0;top:178px;width:1200px;height:120px;background:var(--blue)}
.banner-title{left:90px;top:26px;font-size:27px;line-height:33px;color:#fff}
.banner-title strong{font-weight:700}
.banner-btn{left:942px;top:41px;width:158px;height:39px;border:2px solid #fff;border-radius:4px;color:#fff;font-size:11px;text-align:center;line-height:35px}
.banner-pointer{left:166px;top:298px;width:0;height:0;border-left:11px solid transparent;border-right:11px solid transparent;border-top:11px solid var(--blue);z-index:2}

.hero{left:0;top:298px;width:1200px;height:468px;background:linear-gradient(180deg,#e6e9ec 0%,#bfc4ca 55%,#3a3f47 100%)}

.thumbs{left:0;top:768px;width:1200px;height:126px;background:var(--grey-light)}
.thumb{top:8px;width:199px;height:98px;background:linear-gradient(180deg,#d9dde1,#7f8791)}
.arrow{top:40px}

.about-kicker{left:0;top:932px;width:1200px;text-align:center;font-size:31px;color:var(--blue)}
.about-title{left:0;top:972px;width:1200px;text-align:center;font-size:33px;color:#333}
.about-copy{left:110px;top:1038px;width:980px;text-align:center;font-size:13px;line-height:21px;color:var(--muted)}
.rule{left:98px;top:1124px;width:1004px;height:1px;background:#ddd}

.service{top:1166px;width:320px}
.service-icon{position:absolute;left:0;top:0;width:60px;height:60px;border-radius:50%;display:flex;align-items:center;justify-content:center}
.service-title{position:absolute;left:86px;top:0;font-size:14px;font-weight:600;color:#222;white-space:nowrap}
.service-line{position:absolute;left:86px;top:30px;width:234px;height:1px;background:#ddd}
.service-copy{position:absolute;left:86px;top:50px;width:234px;font-size:12.4px;line-height:20px;color:#444}
.service-btn{position:absolute;left:84px;top:206px;width:118px;height:40px;border:1px solid #cfd5da;background:#e6ebef;border-radius:3px;font-size:12px;text-align:center;line-height:38px;color:#555}
.service-btn.dark{background:var(--grey-btn);border-color:var(--grey-btn);color:#fff}

.dots{left:566px;top:1468px;display:flex;gap:6px}
.dots span{width:11px;height:11px;border-radius:50%;background:#d6d6d6}
.dots span.on{background:#8a8a8a}

.why{left:0;top:1540px;width:1200px;height:384px;background:var(--section-grey)}
.why-media{left:102px;top:60px;width:470px;height:268px;background:linear-gradient(160deg,#c6ccd2 0%,#8e959c 55%,#3b4046 100%)}
.why-media svg{position:absolute;left:200px;top:94px}
.why-title{left:616px;top:60px;font-size:31px;color:#333}
.why-copy{left:616px;top:122px;width:488px;font-size:12.6px;line-height:21px;color:#444}
.btn{top:272px;height:40px;border-radius:3px;font-size:12px;color:#fff;text-align:center;line-height:40px;background:var(--grey-btn)}
.btn.blue{background:var(--blue-soft)}

.steps-title{left:0;top:1960px;width:1200px;text-align:center;font-size:31px;color:#333}
.step-bar{top:2212px;height:52px;color:#fff;font-size:16px;font-weight:600;text-align:center;line-height:52px}
.steps-tag{left:0;top:2306px;width:1200px;text-align:center;font-size:12.5px;color:#444}
.start-btn{left:543px;top:2353px;width:114px;height:40px;border-radius:3px;background:var(--grey-btn);color:#fff;font-size:12px;text-align:center;line-height:40px}

.testimonial{left:0;top:2448px;width:1200px;height:390px}
.testimonial-left{left:0;top:0;width:470px;height:390px;background:var(--blue)}
.testimonial-right{left:470px;top:0;width:730px;height:390px;background:linear-gradient(180deg,#1d2f4e 0%,#4d6f97 45%,#a9c0d8 100%)}
.testimonial-card{left:98px;top:72px;width:658px;height:262px;background:#fff}
.testimonial-card h3{position:absolute;left:48px;top:44px;font-size:20px;font-weight:600;color:var(--blue-soft)}
.testimonial-card p{position:absolute;left:48px;top:104px;width:560px;font-size:12.5px;line-height:21px;font-style:italic;color:#444}
.testimonial-card cite{position:absolute;right:46px;top:186px;font-style:normal;font-size:17px;color:var(--green)}

.site-footer{left:0;top:2838px;width:1200px;height:94px;background:#fff}
.site-footer .brand{left:104px;top:26px}
.site-footer .brand-dot{background:#8f9296}
.site-footer .brand-name{color:#6d7074}
.copyright{right:98px;top:40px;font-size:12px;color:#444}
</style>
</head>
<body>

<header class="site-header abs">
  <div class="brand abs"><span class="brand-dot"></span><span class="brand-name">Harbourline Funding</span></div>
  <div class="search abs">Search
    <svg width="18" height="18" viewBox="0 0 18 18"><circle cx="7.5" cy="7.5" r="5" fill="none" stroke="#333" stroke-width="2"/><line x1="11" y1="11" x2="16" y2="16" stroke="#333" stroke-width="2"/></svg>
  </div>
</header>

<nav class="main-nav abs">
  <a class="current" style="left:94px">HOME</a>
  <a style="left:156px">SERVICES</a>
  <a style="left:232px">WHY HARBOURLINE</a>
  <a style="left:362px">INVESTORS</a>
  <a style="left:449px">ABOUT US</a>
  <a style="left:531px">CONTACT US</a>
  <a style="left:627px">MEMBERS LOGIN</a>
</nav>

<section class="banner abs">
  <h1 class="banner-title abs" style="font-weight:400">Business Taken<br>to The <strong>New Heights</strong></h1>
  <div class="banner-btn abs">READ MORE</div>
</section>
<div class="banner-pointer abs"></div>

<div class="hero abs" role="img" aria-label="Photo of three smiling business people in suits giving thumbs up"></div>

<div class="thumbs abs">
  <svg class="arrow abs" style="left:98px" width="26" height="22" viewBox="0 0 26 22"><path d="M24 11H4M12 3L4 11l8 8" fill="none" stroke="var(--blue)" stroke-width="3"/></svg>
  <div class="thumb abs" style="left:172px" role="img" aria-label="Photo of a businessman"></div>
  <div class="thumb abs" style="left:391px" role="img" aria-label="Photo of a businesswoman on the phone"></div>
  <div class="thumb abs" style="left:610px" role="img" aria-label="Photo of a businesswoman with glasses"></div>
  <div class="thumb abs" style="left:829px" role="img" aria-label="Photo of business people giving thumbs up"></div>
  <svg class="arrow abs" style="left:1076px" width="26" height="22" viewBox="0 0 26 22"><path d="M2 11h20M14 3l8 8-8 8" fill="none" stroke="var(--blue)" stroke-width="3"/></svg>
</div>

<h2 class="about-kicker abs" style="font-weight:400">About us</h2>
<h2 class="about-title abs" style="font-weight:400">Present yourself to the whole world</h2>
<p class="about-copy abs">Contrary to popular belief, Lorem Ipsum is not simply random text. It has roots in a piece of classical Latin literature from 45 BC, making it over 2000 years old. Thomas Aldercott, a Latin professor at Ashgrove College in Virginia</p>
<div class="rule abs"></div>

<article class="service abs" style="left:98px">
  <div class="service-icon" style="background:var(--teal)">
    <svg width="28" height="26" viewBox="0 0 28 26"><path d="M14 2L2 12h4v12h16V12h4z" fill="#fff"/><rect x="11" y="15" width="6" height="9" fill="var(--teal)"/></svg>
  </div>
  <h3 class="service-title">Residential Real Estate Agents</h3>
  <div class="service-line"></div>
  <p class="service-copy">Whether you're a Residential Real Estate Agency or Agent we understand that with residential real estate transactions settling on average in 42 days that your well earned and outstanding commissions ...</p>
  <div class="service-btn">Read More</div>
</article>
<article class="service abs" style="left:442px">
  <div class="service-icon" style="background:var(--green)">
    <svg width="30" height="30" viewBox="0 0 30 30"><circle cx="15" cy="15" r="4" fill="#fff"/><g stroke="#fff" stroke-width="2"><line x1="15" y1="3" x2="15" y2="9"/><line x1="15" y1="21" x2="15" y2="27"/><line x1="3" y1="15" x2="9" y2="15"/><line x1="21" y1="15" x2="27" y2="15"/><line x1="6" y1="6" x2="10" y2="10"/><line x1="20" y1="20" x2="24" y2="24"/><line x1="24" y1="6" x2="20" y2="10"/><line x1="10" y1="20" x2="6" y2="24"/></g></svg>
  </div>
  <h3 class="service-title">Commercial Real Estate Agents</h3>
  <div class="service-line"></div>
  <p class="service-copy">Whether you're a Commercial Real Estate Agency or Agent we understand that with commercial real estate transactions settling at all different periods that well earned and outstanding commissions ...</p>
  <div class="service-btn dark">Read More</div>
</article>
<article class="service abs" style="left:784px">
  <div class="service-icon" style="background:var(--red)">
    <svg width="26" height="26" viewBox="0 0 26 26"><g fill="#fff"><ellipse cx="13" cy="6" rx="9" ry="3.5"/><rect x="4" y="9" width="18" height="4" rx="2"/><rect x="4" y="15" width="18" height="4" rx="2"/><rect x="4" y="21" width="18" height="4" rx="2"/></g></svg>
  </div>
  <h3 class="service-title">Mortgage &amp; Finance Brokers</h3>
  <div class="service-line"></div>
  <p class="service-copy">Whether you're a mortgage broker focusing on home loans or a finance broker operating in different area's of finance we have a deep understanding of your industry and the nuances involved, especially ...</p>
  <div class="service-btn">Read More</div>
</article>

<div class="dots abs"><span></span><span></span><span class="on"></span><span></span></div>

<section class="why abs">
  <div class="why-media abs" role="img" aria-label="Video still of a laptop and tablet on a desk with a coffee cup">
    <svg width="70" height="70" viewBox="0 0 70 70"><circle cx="35" cy="35" r="30" fill="rgba(0,0,0,.35)" stroke="#fff" stroke-width="5"/><path d="M28 22l20 13-20 13z" fill="#fff"/></svg>
  </div>
  <h2 class="why-title abs" style="font-weight:400">Why Harbourline Funding</h2>
  <p class="why-copy abs">At Harbourline Funding our aim is to provide immediate commission advance solutions for all industries. Our background is sales, property and finance and we understand the issues faced with Small to medium Businesses, Agents, contractors and consultants who earn commissions. Unforeseen expenses, inconstant sales, holiday periods, sickness, taxation bills and job changes can all have an effect on a sales and commission flow.</p>
  <div class="btn abs" style="left:614px;width:114px">Read More</div>
  <div class="btn blue abs" style="left:741px;width:172px">Our Pricing Guaranted</div>
  <div class="btn abs" style="left:928px;width:170px">Our Loyalty Program</div>
</section>

<h2 class="steps-title abs" style="font-weight:400">3 Easy Steps To a Stress Free Solution</h2>
<svg class="abs" style="left:0;top:2040px" width="1200" height="180" viewBox="0 0 1200 180">
  <g fill="#fff" stroke-width="6">
    <circle cx="256" cy="120" r="80" stroke="var(--blue-soft)"/>
    <circle cx="602" cy="108" r="88" stroke="var(--green)"/>
    <circle cx="946" cy="120" r="80" stroke="var(--blue-soft)"/>
  </g>
  <g font-family="Open Sans, Arial, sans-serif" font-size="52" font-weight="600" text-anchor="middle">
    <text x="256" y="141" fill="var(--blue-soft)">01</text>
    <text x="602" y="129" fill="var(--green)">02</text>
    <text x="946" y="141" fill="var(--blue-soft)">03</text>
  </g>
</svg>
<div class="step-bar abs" style="left:100px;width:314px;background:var(--blue-soft)">Call or click</div>
<div class="step-bar abs" style="left:442px;width:314px;background:var(--green)">Fill out &amp; Sign</div>
<div class="step-bar abs" style="left:784px;width:316px;background:var(--blue-soft)">Funds in bank in 4 hours</div>
<p class="steps-tag abs">A hassle free finance solution that grows as your business grows</p>
<div class="start-btn abs">Start Now</div>

<section class="testimonial abs">
  <div class="testimonial-left abs"></div>
  <div class="testimonial-right abs" role="img" aria-label="Photo of a young businessman launching a paper plane against a blue sky"></div>
  <div class="testimonial-card abs">
    <h3>What people say about us</h3>
    <p>" The service was beyond my expectations. But please, replace this with an actual customer testimonial, this is just for testing purposes ".</p>
    <cite>Dana Whitfield, Brightside Trading LLC</cite>
  </div>
</section>

<footer class="site-footer abs">
  <div class="brand abs"><span class="brand-dot"></span><span class="brand-name">Harbourline Funding</span></div>
  <p class="copyright abs">Copyright © 2016, All Right Reserved</p>
</footer>

</body>
</html>
```